Brasko Construction Business Card

I need a business card design for my company.
We are a construction/machinery company.
I would like to see my logo on the front of the card and my details on the other side
I would like the card to be black or dark grey in colour,with my logo as i send it or modified with a lighter blue colour
I would like to see the design kept fairly simple,but eye catching at the same time
Industry/Entity Type
Business
Contact Information for Business Card
Name
Phone Number
Address
Email
Colors
00a990
1b1b1b
000000
474747
ececec

```html
<!DOCTYPE html>
<html lang="en">
<head>
<meta charset="utf-8">
<title>Brasko Construction Business Card</title>
<link rel="stylesheet" href="https://fonts.googleapis.com/css2?family=Open+Sans:wght@400;600;700;800&display=swap">
<style>
  :root {
    --teal: #00a990;
    --ink: #1b1b1b;
    --black: #000000;
    --graphite: #474747;
    --paper: #ffffff;
    --mist: #ececec;
    --backdrop: #e4e4e4;
  }
  html, body {
    margin: 0;
    padding: 0;
    width: 1200px;
    height: 913px;
    overflow: hidden;
    background: var(--backdrop);
    font-family: "Open Sans", Arial, sans-serif;
  }
  .canvas {
    position: relative;
    width: 1200px;
    height: 913px;
  }
  .card {
    position: absolute;
    width: 500px;
    height: 286px;
    border-radius: 18px;
    overflow: hidden;
    box-shadow: 0 12px 30px rgba(0,0,0,0.25);
  }
  .card--front { left: 80px; top: 140px; }
  .card--back { left: 620px; top: 470px; }
  .card__art {
    position: absolute;
    inset: 0;
    width: 100%;
    height: 100%;
  }
  .brand-mark {
    position: absolute;
    left: 40px;
    top: 46px;
    width: 250px;
    display: flex;
    align-items: center;
    gap: 10px;
    color: var(--ink);
    font-weight: 800;
    font-size: 22px;
    letter-spacing: 1px;
    text-transform: uppercase;
    line-height: 1.1;
  }
  .brand-mark__square {
    width: 26px;
    height: 26px;
    background: var(--ink);
    flex: none;
  }
  .holder {
    position: absolute;
    left: 44px;
    top: 226px;
    color: var(--paper);
  }
  .holder__name {
    font-size: 19px;
    font-weight: 700;
    margin: 0;
    line-height: 1.1;
  }
  .holder__role {
    font-size: 12px;
    color: var(--teal);
    margin: 2px 0 0;
  }
  .contact {
    position: absolute;
    right: 22px;
    top: 178px;
    margin: 0;
    padding: 0;
    list-style: none;
    color: var(--paper);
    font-size: 12px;
    text-align: right;
  }
  .contact li {
    display: flex;
    justify-content: flex-end;
    align-items: center;
    gap: 8px;
    height: 19px;
  }
  .contact svg { width: 10px; height: 10px; flex: none; }
  .back-name {
    position: absolute;
    left: 250px;
    top: 150px;
    width: 220px;
    text-align: center;
    color: var(--paper);
    font-weight: 800;
    font-size: 26px;
    letter-spacing: 1px;
    text-transform: uppercase;
    line-height: 1.1;
  }
</style>
</head>
<body>
<main class="canvas">

  <section class="card card--front" aria-label="Business card, details side">
    <svg class="card__art" viewBox="0 0 500 286" aria-hidden="true">
      <rect width="500" height="286" fill="var(--paper)"/>
      <path d="M0,209 C200,189 330,84 500,24 L500,286 L0,286 Z" fill="var(--teal)"/>
      <path d="M0,215 C200,195 330,90 500,30 L500,286 L0,286 Z" fill="var(--ink)"/>
      <line x1="140" y1="205" x2="480" y2="130" stroke="var(--graphite)" stroke-width="1"/>
      <path d="M0,222 A22,22 0 0 1 0,266 Z" fill="var(--teal)"/>
    </svg>

    <div class="brand-mark">
      <span class="brand-mark__square"></span>
      <span>Brasko Construction</span>
    </div>

    <div class="holder">
      <p class="holder__name">Lena Marsh</p>
      <p class="holder__role">Director</p>
    </div>

    <ul class="contact">
      <li>+41 3817-5512
        <svg viewBox="0 0 10 10"><path d="M2,0.5 L3.8,2.6 L3,3.8 Q4.2,6 6.2,7 L7.4,6.2 L9.5,8 L8.3,9.5 Q3.5,9 0.5,1.7 Z" fill="var(--teal)"/></svg>
      </li>
      <li>info@braskobuild.com
        <svg viewBox="0 0 10 10"><rect x="0.5" y="2" width="9" height="6.5" fill="none" stroke="var(--teal)"/><path d="M0.5,2 L5,5.5 L9.5,2" fill="none" stroke="var(--teal)"/></svg>
      </li>
      <li>48 Ridge Street Harlow NSW 2841
        <svg viewBox="0 0 10 10"><path d="M5,9.8 L1.8,5 A3.6,3.6 0 1 1 8.2,5 Z" fill="var(--teal)"/><circle cx="5" cy="3.6" r="1.3" fill="var(--ink)"/></svg>
      </li>
    </ul>
  </section>

  <section class="card card--back" aria-label="Business card, logo side">
    <svg class="card__art" viewBox="0 0 500 286" aria-hidden="true">
      <rect width="500" height="286" fill="var(--paper)"/>
      <path d="M0,250 Q250,170 500,62 L500,286 L0,286 Z" fill="var(--teal)"/>
      <path d="M0,257 Q250,178 500,70 L500,286 L0,286 Z" fill="var(--black)"/>
    </svg>
    <div class="back-name">Brasko Construction</div>
  </section>

</main>
</body>
</html>
```